Business card for design-ceiling company
Brookvale Ceiling
Business card for design-ceiling company - Construction
Creative Brief
Bright & Fun-filled
Marisol Venkataraman
President
4th Floor, TORVIN Building, 2714 Eduardo Quilantang Ave. corner J. Barrientos, St., Sta. Lucia, Manila, Metro Manila
hello@brookvaleceiling.example
www.brookvaleceiling.example
"Brookvale Ceiling - when technology and art become one." or full size logo
Gotesco Gotesco
Good day designers! Also I want to put advantages of the product on the back of the card Advantages 1 Quick installation (1-2 days) 2 Clean installation: No dirt, No smell 3 Doesn’t require painting 4 Easy to clean with any ordinary cleaners 5 Waterproof material 6 It is protection from flood! 7 Non-flammable, Fire resistant 8 Zero risk of cracking 9 Ceiling always perfectly glide 10 Always perfect color 11 Excellent light reflection 12 Excellent acoustic properties 13 Non Toxic & Cadmium Free 14 100% Recyclable

```html
<!DOCTYPE html>
<html lang="en">
<head>
<meta charset="utf-8">
<title>Brookvale Ceiling – Business Card</title>
<link rel="stylesheet" href="https://fonts.googleapis.com/css2?family=Cinzel:wght@500&family=Open+Sans:ital,wght@0,400;0,600;1,400&display=swap">
<style>
  :root {
    --stage: #e6e4e1;
    --card-white: #ffffff;
    --copper: #b98a66;
    --copper-light: #e2c2a6;
    --copper-dark: #8f6344;
    --ink: #3b3633;
    --muted: #7d7773;
    --shadow: rgba(0,0,0,0.18);
  }
  * { box-sizing: border-box; margin: 0; padding: 0; }
  html, body { width: 1200px; height: 901px; overflow: hidden; }
  body {
    background: var(--stage);
    font-family: "Open Sans", Arial, sans-serif;
    display: flex;
    flex-direction: column;
    align-items: center;
    justify-content: center;
    gap: 40px;
  }
  .card {
    width: 700px;
    height: 400px;
    position: relative;
    overflow: hidden;
    box-shadow: 0 6px 18px var(--shadow);
  }

  /* Back side */
  .card-back .pattern-fill {
    position: absolute; inset: 0;
    background: linear-gradient(120deg, var(--copper-dark) 0%, var(--copper) 45%, var(--copper-light) 70%, var(--copper) 100%);
  }
  .card-back .back-mark {
    position: absolute;
    right: 150px; top: 150px;
    color: var(--card-white);
    font-family: "Cinzel", Georgia, serif;
    font-weight: 500;
    font-size: 26px;
    letter-spacing: 2px;
    line-height: 1.1;
    text-transform: uppercase;
  }

  /* Front side */
  .card-front { background: var(--card-white); }
  .brand {
    position: absolute; left: 44px; top: 34px;
    display: flex; align-items: center; gap: 14px;
    color: var(--copper);
    font-family: "Cinzel", Georgia, serif;
    font-weight: 500;
    font-size: 28px;
    line-height: 1;
    letter-spacing: 2px;
    text-transform: uppercase;
  }
  .brand-dot {
    width: 14px; height: 14px; border-radius: 50%;
    background: var(--copper);
  }
  .name-band {
    position: absolute; left: 0; top: 122px;
    width: 100%; height: 46px;
    background: linear-gradient(90deg, var(--copper-light) 0%, var(--copper) 55%, var(--copper-light) 100%);
  }
  .person-name {
    position: absolute; left: 44px; top: 131px;
    color: var(--ink);
    font-weight: 600;
    font-size: 21px;
  }
  .person-title {
    position: absolute; left: 44px; top: 174px;
    color: var(--muted);
    font-style: italic;
    font-size: 13px;
  }
  .address {
    position: absolute; left: 44px; top: 248px;
    width: 250px;
    color: var(--muted);
    font-style: italic;
    font-size: 13px;
    line-height: 1.45;
  }
  .divider {
    position: absolute; left: 316px; top: 252px;
    width: 1px; height: 78px;
    background: var(--muted);
  }
  .contacts {
    position: absolute; left: 330px; top: 252px;
    list-style: none;
    color: var(--muted);
    font-size: 13px;
  }
  .contacts li {
    display: flex; align-items: center; gap: 8px;
    height: 26px;
  }
  .contacts svg { width: 14px; height: 14px; fill: var(--copper); }
</style>
</head>
<body>

<section class="card card-back">
  <div class="pattern-fill" role="img" aria-label="Copper background with a repeating brand monogram pattern"></div>
  <div class="back-mark">Brookvale<br>Ceiling</div>
</section>

<section class="card card-front">
  <div class="brand">
    <span class="brand-dot"></span>
    <span>Brookvale<br>Ceiling</span>
  </div>

  <div class="name-band"></div>
  <h1 class="person-name">Marisol Venkataraman</h1>
  <p class="person-title">President</p>

  <address class="address">
    4th Floor, TORVIN Building, 2714 Eduardo Quilantang Ave. corner J. Barrientos, St., Sta. Lucia, Manila, Metro Manila
  </address>

  <div class="divider"></div>

  <ul class="contacts">
    <li>
      <svg viewBox="0 0 24 24" aria-hidden="true"><path d="M6.6 10.8a15.1 15.1 0 0 0 6.6 6.6l2.2-2.2c.3-.3.7-.4 1-.2 1.1.4 2.3.6 3.6.6.6 0 1 .4 1 1V20c0 .6-.4 1-1 1A17 17 0 0 1 3 4c0-.6.4-1 1-1h3.5c.6 0 1 .4 1 1 0 1.3.2 2.5.6 3.6.1.3 0 .7-.2 1z"/></svg>
      <span>+6325550147</span>
    </li>
    <li>
      <svg viewBox="0 0 24 24" aria-hidden="true"><path d="M3 5h18v14H3zm2 2v.4l7 4.6 7-4.6V7zm0 2.8V17h14V9.8l-7 4.6z"/></svg>
      <span>hello@brookvaleceiling.example</span>
    </li>
    <li>
      <svg viewBox="0 0 24 24" aria-hidden="true"><path d="M12 2a10 10 0 1 0 0 20 10 10 0 0 0 0-20zm6.9 9h-3a15 15 0 0 0-1.3-5.6A8 8 0 0 1 18.9 11zM12 4c.9 1.2 1.8 3.6 1.9 7h-3.8c.1-3.4 1-5.8 1.9-7zM9.4 5.4A15 15 0 0 0 8.1 11h-3a8 8 0 0 1 4.3-5.6zM5.1 13h3a15 15 0 0 0 1.3 5.6A8 8 0 0 1 5.1 13zM12 20c-.9-1.2-1.8-3.6-1.9-7h3.8c-.1 3.4-1 5.8-1.9 7zm2.6-1.4a15 15 0 0 0 1.3-5.6h3a8 8 0 0 1-4.3 5.6z"/></svg>
      <span>www.brookvaleceiling.example</span>
    </li>
  </ul>
</section>

</body>
</html>
```